Mesh Banner Design for Business Premises

We require the design of a large mesh banner to be installed across the front fence of our warehouse. The banner should prominently feature our existing Trelborn logo and brand colours (yellow, white, and black) and be designed to be highly visible from the road.

The overall aesthetic should be strong, masculine, and industrial, reflecting the nature of the scaffolding and construction industry. The background should be predominantly black, with our branding incorporated in yellow and white for strong contrast and readability.

The banner should clearly communicate the full scope of services we provide, including:

Scaffold Design
Scaffold Engineering
Scaffold Installation / Erection
Scaffold Dismantling

It should also indicate the types of projects and clients we service, including:

Commercial
Industrial
Residential
Civil

The design should feel bold and professional, with a construction-oriented style that aligns with the scaffolding industry. It should be clean, impactful, and easy to read from a distance, ensuring passing traffic can quickly understand our services.

Where possible, subtle industrial or structural design elements (such as scaffold components, steel textures, or linework) may be incorporated into the background to reinforce the industry theme while keeping the layout uncluttered.

The final design will be produced as a large-format mesh banner for outdoor installation, so it should be created with this application and viewing distance in mind.

```html
<!DOCTYPE html>
<html lang="en">
<head>
<meta charset="utf-8">
<title>Trelborn Mesh Banner</title>
<link rel="stylesheet" href="https://fonts.googleapis.com/css2?family=Roboto+Condensed:wght@400;700&display=swap">
<style>
  :root {
    --stage: #e4e4e4;
    --banner-black: #272727;
    --brand-yellow: #f8ae21;
    --ink-dark: #2a2a2a;
  }
  * { box-sizing: border-box; margin: 0; padding: 0; }
  html, body {
    width: 1200px;
    height: 1200px;
    overflow: hidden;
    background: var(--stage);
  }
  .canvas {
    position: relative;
    width: 1200px;
    height: 1200px;
  }
  .banner {
    position: absolute;
    left: 30px;
    top: 363px;
    width: 1140px;
    height: 473px;
    background: var(--banner-black);
    font-family: "Roboto Condensed", "Arial Narrow", sans-serif;
  }
  .brand {
    position: absolute;
    left: 81px;
    top: 49px;
    width: 357px;
    height: 264px;
    display: flex;
    align-items: center;
    justify-content: center;
  }
  .brand-name {
    color: var(--brand-yellow);
    font-weight: 700;
    font-size: 82px;
    letter-spacing: 1px;
  }
  .services-panel {
    position: absolute;
    left: 516px;
    top: 22px;
    width: 624px;
    height: 338px;
    background: var(--brand-yellow);
  }
  .services-list {
    position: absolute;
    left: 65px;
    top: 66px;
    list-style: none;
    color: var(--ink-dark);
    font-weight: 400;
    font-size: 37px;
    line-height: 44.5px;
  }
  .services-list li::before {
    content: "\2022";
    display: inline-block;
    width: 22px;
  }
  .sectors {
    position: absolute;
    left: 0;
    right: 0;
    top: 381px;
    text-align: center;
    color: var(--brand-yellow);
    font-weight: 700;
    font-size: 41px;
    line-height: 48px;
  }
</style>
</head>
<body>
  <main class="canvas">
    <section class="banner">
      <div class="brand">
        <span class="brand-name">Trelborn</span>
      </div>
      <div class="services-panel">
        <ul class="services-list">
          <li>Scaffold Design</li>
          <li>Scaffold Engineering</li>
          <li>Scaffold Installation / Erection</li>
          <li>Scaffold Dismantling</li>
        </ul>
      </div>
      <p class="sectors">Commercial &bull; Industrial &bull; Residential &bull; Civil</p>
    </section>
  </main>
</body>
</html>
```